A Speech Therapy Business needs to update their logo

I need an update to the font and color of my logo to look more appealing. I am looking to open a private practice as a Speech Language Pathologist that caters to adults and children. It needs to be sophisticated and friendly at the same time. I want to keep the silhouette in my logo as is, just update the font and color for "Brightpaths".
Industry/Entity Type
Business
Contact Information for Business Card
I want the business card to have my logo, my name (Dorota Valk, CCC-SLP, TSSLD) and that I am a Bilingual Speech Language Pathologist. Also, include my phone number, (555) 271-8390. Include my website, Brightpathsslp.example, and email address, dorotavalk@brightpathsslp.example
Look and feel
Each slider illustrates characteristics of the customer's brand and the style your logo design should communicate.

```html
<!DOCTYPE html>
<html lang="en">
<head>
<meta charset="utf-8">
<title>Brightpaths – Business Card</title>
<link rel="stylesheet" href="https://fonts.googleapis.com/css2?family=Open+Sans:wght@300;400;600;700&display=swap">
<style>
  :root {
    --backdrop: #e9e7e3;
    --card: #ffffff;
    --accent: #29abe2;
    --accent-soft: #9fd8f1;
    --ink: #2b2b2b;
    --ink-soft: #555555;
    --figure-dark: #1f1f1f;
    --figure-mid: #6d6d6d;
  }
  * { box-sizing: border-box; margin: 0; padding: 0; }
  html, body {
    width: 1200px;
    height: 1022px;
    overflow: hidden;
    background: var(--backdrop);
    font-family: "Open Sans", Arial, sans-serif;
  }
  .canvas {
    width: 1200px;
    height: 1022px;
    display: flex;
    align-items: center;
    justify-content: center;
  }
  .business-card {
    position: relative;
    width: 900px;
    height: 514px;
    background: var(--card);
    box-shadow: 0 10px 30px rgba(0,0,0,0.12);
    display: flex;
    align-items: center;
  }
  .brand {
    width: 470px;
    padding-left: 60px;
    display: flex;
    flex-direction: column;
    align-items: flex-start;
  }
  .brand-figures {
    width: 360px;
    height: 120px;
    background: linear-gradient(90deg, var(--figure-dark), var(--figure-mid));
    border-radius: 4px;
  }
  .brand-name {
    margin-top: 14px;
    font-size: 74px;
    font-weight: 300;
    color: var(--accent);
    letter-spacing: 1px;
    line-height: 1;
  }
  .divider {
    width: 2px;
    height: 240px;
    background: linear-gradient(180deg, var(--accent), var(--accent-soft));
  }
  .details {
    padding-left: 34px;
    color: var(--ink);
  }
  .person-name {
    font-size: 30px;
    font-weight: 700;
    color: var(--accent);
    letter-spacing: 2px;
    text-transform: uppercase;
  }
  .credentials, .role {
    font-size: 19px;
    color: var(--ink-soft);
    line-height: 1.45;
  }
  .contact-list {
    list-style: none;
    margin-top: 22px;
  }
  .contact-item {
    display: flex;
    align-items: center;
    gap: 12px;
    font-size: 18px;
    line-height: 1.7;
    color: var(--ink);
  }
  .contact-icon { width: 16px; height: 16px; flex: none; }
  .web-highlight { color: var(--accent); font-weight: 700; }
</style>
</head>
<body>
<main class="canvas">
  <section class="business-card">
    <div class="brand">
      <div class="brand-figures" role="img" aria-label="Silhouettes of people of growing ages walking in a row, from toddler to adult"></div>
      <div class="brand-name">Brightpaths</div>
    </div>
    <div class="divider"></div>
    <div class="details">
      <h1 class="person-name">Dorota Valk</h1>
      <p class="credentials">CCC-SLP, TSSLD</p>
      <p class="role">Bilingual Speech Language Pathologist</p>
      <ul class="contact-list">
        <li class="contact-item">
          <svg class="contact-icon" viewBox="0 0 16 16"><path d="M4 1l3 3-2 2c1 2 3 4 5 5l2-2 3 3-2 3C7 15 1 9 1 3z" fill="#29abe2"/></svg>
          (555) 271-8390
        </li>
        <li class="contact-item">
          <svg class="contact-icon" viewBox="0 0 16 16"><rect x="1" y="3" width="14" height="10" fill="none" stroke="#29abe2" stroke-width="1.6"/><path d="M1 3l7 6 7-6" fill="none" stroke="#29abe2" stroke-width="1.6"/></svg>
          dorotavalk@brightpathsslp.example
        </li>
        <li class="contact-item">
          <svg class="contact-icon" viewBox="0 0 16 16"><circle cx="8" cy="8" r="6.5" fill="none" stroke="#29abe2" stroke-width="1.5"/><ellipse cx="8" cy="8" rx="3" ry="6.5" fill="none" stroke="#29abe2" stroke-width="1.2"/><path d="M1.5 8h13" stroke="#29abe2" stroke-width="1.2"/></svg>
          <span>www.<span class="web-highlight">brightpathsslp</span>.example</span>
        </li>
      </ul>
    </div>
  </section>
</main>
</body>
</html>
```